依頼詳細
PCとスマホデザインの両方納品をいただきますが、
まずはデザインイメージが確認しやすいPCページのみの提案をお願いします。
スマホページは当選者に納品時にお願いしたいと思います。
スマホサイズについて、カンバスサイズは横幅375pxで作成し、2倍の横幅750pxのサイズで書き出ししてください。
(Retinaディスプレイに対応するため)
スマホページ作成時は、メニューが展開した際のデザインもお願いします。
レスポンシブウェブデザインを意識したデザインでお願いします。

■サイトマップ
添付の画面遷移図をご確認ください。

■参考サイト
https://www.hirotoku-sarumi.jp/
https://www.tabuse-seiban.co.jp/

■内容について
主に鋼材の卸売業を行う会社の公式サイトになります。
卸売だけでなく、鋼板を仕入れて希望のサイズに切断、プレスなどの加工も行う会社です。
参考サイトはメインビジュアルが動画になっていますが、今回のサイトデザインでは動画を使用する予定は今のところありません。

■素材写真
画像データについては、フリー素材から流用して
イメージ画像に当て込んでください。
足りない場合は、一旦他のサイトの写真をサンプルとして
入れてください。(サンプルなどの表記をお願いします)
また、購入が必要な写真などを利用した場合、
価格とサイト名を教えてください。

また、Pixoral Imageで定期契約をしていますので、
Pixoral Imageの画像は使用できます。
デザイン時はカンプ画像をお入れいただきますようお願いします。

■ロゴについて
添付のロゴデータを使用してください。

■ワイヤーフレーム
https://mock.velqara.net/view/52817caa-1f3b-4d0e-9a72-6e1b8c37d904-b39f/?fullscreen
コンテンツの構成としてワイヤーフレームを作成しましたが
必ずしもワイヤーフレームの通りではなくて大丈夫です。
TOPページに配置するコンテンツを見ていただき、デザインは
デザイナーの皆様におまかせしたいと思います。

----------------------------------------------------------------------------
【制作物に対するお願い】

■フォントについて
・無料で使えるフォントで作成をお願いします。
・OSに紐づくフォントの使用は控えていただければと思います (ヒラギノなど)

ページ数
1ページ
希望イメージ
シンプル 複雑
単色 カラフル
暗い 明るい
日常 高級
遊び心 厳粛
未来的 伝統的
女性的 男性的
希望する色
ベースカラー:白、青、ポイントカラー:赤
納品ファイル
• 高解像度JPG (.jpg)
• イラストレーター形式 (.ai)
• フォトショップ形式 (.psd)
補足説明
上記のいずれか1つ(アウトラインありとなしの2つ)と高解像度JPGを納品お願いします。
adobe XDでの納品も可能です。
CS5にバージョンを落としたロゴデータです。
ロゴのpngデータも追加しました。

```html
<!DOCTYPE html>
<html lang="ja">
<head>
<meta charset="UTF-8">
<title>北陽スチール株式会社</title>
<link rel="stylesheet" href="https://fonts.googleapis.com/css2?family=Noto+Sans+JP:wght@400;500;700;900&family=Montserrat:wght@500;700&display=swap">
<style>
:root{
  --blue:#2a35c9;
  --navy:#1a1f6e;
  --red:#e0141e;
  --ink:#222;
  --muted:#555;
  --ghost:#ececec;
  --white:#fff;
}
*{margin:0;padding:0;box-sizing:border-box}
html,body{width:1200px;height:2436px;overflow:hidden;background:var(--white)}
body{position:relative;font-family:"Noto Sans JP",sans-serif;color:var(--ink)}
.abs{position:absolute}

.site-header{left:0;top:0;width:1200px;height:56px;background:var(--white);z-index:5}
.brand{left:30px;top:16px;font-size:17px;font-weight:700;color:var(--red);display:flex;align-items:center;gap:8px}
.brand .mark{width:14px;height:14px;background:var(--red)}
.global-nav{left:650px;top:0;height:56px;display:flex;gap:44px;align-items:center;font-size:13px;font-weight:500}
.contact-btn{left:920px;top:0;width:160px;height:52px;background:var(--red);color:var(--white);font-size:13px;font-weight:700;display:flex;align-items:center;justify-content:center}

.hero{left:0;top:0;width:1200px;height:620px;background:radial-gradient(circle at 58% 28%,#f3a64a 0,#b3652a 10%,#3b3a44 34%,#1d2230 70%,#0f121a 100%)}
.hero-copy{left:140px;top:280px;color:var(--white);font-size:32px;font-weight:700;line-height:1.6;letter-spacing:.04em}

.ghost{font-family:"Montserrat",sans-serif;font-weight:700;font-size:120px;color:var(--ghost);letter-spacing:.04em;line-height:1}
.sec-title{font-size:28px;font-weight:700;color:var(--blue);letter-spacing:.04em}
.lead{font-size:16px;font-weight:700}
.body{font-size:12px;line-height:2;color:var(--muted);width:450px}
.btn{height:32px;background:var(--blue);color:var(--white);font-size:12px;display:flex;align-items:center;justify-content:center;gap:10px}

.photo{background:linear-gradient(135deg,#6b6d74,#2d3038)}
.offset{background:var(--blue)}
.recruit-photo{left:0;top:1400px;width:1200px;height:360px;background:linear-gradient(90deg,#2a3060,#3e4690 45%,#6a6f96)}

.to-top{left:1020px;top:2112px;width:44px;height:44px;background:var(--navy)}

.site-footer{left:0;top:2180px;width:1200px;height:256px;background:var(--blue);color:var(--white)}
.f-brand{left:140px;top:34px;font-size:17px;font-weight:700;display:flex;align-items:center;gap:8px}
.f-brand .mark{width:14px;height:14px;background:var(--white)}
.f-addr{left:140px;top:66px;font-size:11px;line-height:1.8}
.contact-box{left:470px;top:30px;width:510px;height:80px;background:var(--white);color:var(--ink)}
.contact-box .q{left:30px;top:14px;font-size:14px;font-weight:700}
.contact-box .tel{left:30px;top:38px;font-family:"Montserrat",sans-serif;font-size:28px;font-weight:700;color:var(--red);display:flex;align-items:center;gap:6px}
.contact-box .hours{left:245px;top:50px;font-size:11px;color:var(--muted)}
.mail{left:980px;top:30px;width:80px;height:80px;background:var(--red);display:flex;flex-direction:column;align-items:center;justify-content:center;gap:4px;font-size:11px;font-weight:700}
.f-nav{left:140px;top:198px;display:flex;gap:40px;font-size:11px}
.copy{left:0;top:232px;width:1200px;text-align:center;font-size:10px}
</style>
</head>
<body>

<div class="abs hero" role="img" aria-label="火花を散らしながら鋼材を切断する作業の写真"></div>
<p class="abs hero-copy">鋼板を希望のサイズに切断、<br>プレス加工にも対応</p>

<header class="abs site-header">
  <div class="abs brand"><span class="mark"></span>北陽スチール株式会社</div>
  <nav class="abs global-nav"><span>事業内容</span><span>会社概要</span><span>採用情報</span></nav>
  <div class="abs contact-btn">お問い合わせ</div>
</header>

<section>
  <div class="abs ghost" style="left:130px;top:640px">ABOUT</div>
  <h2 class="abs sec-title" style="left:140px;top:790px">北陽スチールについて</h2>
  <p class="abs lead" style="left:580px;top:672px">テキストが入ります。テキストが入ります。</p>
  <p class="abs body" style="left:580px;top:716px">テキストが入ります。テキストが入ります。テキストが入ります。テキストが入ります。テキストが入ります。テキストが入ります。テキストが入ります。テキストが入ります。テキストが入ります。テキストが入ります。テキストが入ります。テキストが入ります。テキストが入ります。テキストが入ります。テキストが入ります。テキストが入ります。テキストが入ります。テキストが入ります。</p>
  <div class="abs btn" style="left:640px;top:916px;width:140px">事業内容 ›</div>
  <div class="abs btn" style="left:828px;top:916px;width:180px">会社概要 ›</div>

  <div class="abs offset" style="left:124px;top:1016px;width:440px;height:360px"></div>
  <div class="abs photo" style="left:140px;top:1000px;width:440px;height:360px" role="img" aria-label="積み重ねられた鋼板の写真"></div>
  <div class="abs offset" style="left:636px;top:1016px;width:424px;height:360px"></div>
  <div class="abs photo" style="left:620px;top:1000px;width:424px;height:360px;background:linear-gradient(135deg,#8a8c90,#3a3c42)" role="img" aria-label="金属を加工する工作機械の写真"></div>
</section>

<section>
  <div class="abs recruit-photo" role="img" aria-label="フォークリフトで作業する倉庫の写真"></div>
  <div class="abs ghost" style="left:130px;top:1745px">RECRUIT</div>
  <h2 class="abs sec-title" style="left:140px;top:1930px">採用情報</h2>
  <p class="abs lead" style="left:580px;top:1850px">テキストが入ります。テキストが入ります。</p>
  <p class="abs body" style="left:580px;top:1894px">テキストが入ります。テキストが入ります。テキストが入ります。テキストが入ります。テキストが入ります。テキストが入ります。テキストが入ります。テキストが入ります。テキストが入ります。テキストが入ります。テキストが入ります。テキストが入ります。テキストが入ります。テキストが入ります。</p>
  <div class="abs btn" style="left:580px;top:2060px;width:190px">採用情報 ›</div>
  <div class="abs to-top"><svg width="44" height="44" viewBox="0 0 44 44"><path d="M16 25l6-6 6 6" fill="none" stroke="#fff" stroke-width="2"/></svg></div>
</section>

<footer class="abs site-footer">
  <div class="abs f-brand"><span class="mark"></span>北陽スチール株式会社</div>
  <p class="abs f-addr">〒955-0000　新潟県三条市北陽町1-2-3<br>TEL. 0256-55-0182<br>FAX. 0256-55-0183</p>
  <div class="abs contact-box">
    <p class="abs q">ご相談やご依頼など、お気軽にお問い合わせください。</p>
    <p class="abs tel"><svg width="22" height="22" viewBox="0 0 24 24"><path d="M6.6 10.8a15 15 0 006.6 6.6l2.2-2.2a1 1 0 011-.25 11 11 0 003.6.6 1 1 0 011 1V20a1 1 0 01-1 1A17 17 0 013 4a1 1 0 011-1h3.5a1 1 0 011 1 11 11 0 00.6 3.6 1 1 0 01-.25 1z" fill="#e0141e"/></svg>0256-55-0182</p>
    <p class="abs hours">受付時間 8:00〜17:00（土日祝除く）</p>
  </div>
  <div class="abs mail"><svg width="26" height="20" viewBox="0 0 26 20"><rect x="1" y="1" width="24" height="18" fill="none" stroke="#fff" stroke-width="2"/><path d="M1 1l12 10L25 1" fill="none" stroke="#fff" stroke-width="2"/></svg>メール</div>
  <nav class="abs f-nav"><span>TOPページ</span><span>事業内容</span><span>会社概要</span><span>採用情報</span><span>お問い合わせ</span><span>プライバシーポリシー</span><span>サイトマップ</span></nav>
  <p class="abs copy">Copyright © 北陽スチール All Rights Reserved.</p>
</footer>

</body>
</html>
```